Keystone Vault Depot Services Needs A Website

We are looking for a website for a new company. 4 Pages

Needs to be responsive and mobile friendly for all browsers and coded for both Android & IOS. SEO is also important.

Website Brief – Keystone Vault Depot Services
Domain: www.keystonevaultdepot.com
Email: info@keystonevaultdepot.com
Phone: to be inserted later
Address: 10458 82 Ave, Edmonton, AB T6E 2K9
Platform: WordPress (recommended for flexibility, SEO tools, and ease of editing)
Requirements:
• Responsive & mobile-friendly (Android & iOS)
• Cross-browser compatibility
• Fast page load speed
• SEO optimized for storage development, management, and investment keywords
• Easy in-house editing after launch
• Professional, modern, trust-driven design reflecting expertise, reliability, and innovation
________________________________________
Pages
1. HOME
Purpose: Quickly communicate who Keystone Vault Depot Services is and why they’re the best choice for designing, building, leasing, and managing self storage facilities.
Content Highlights:
• Hero Section: Large, bold image of a modern self storage facility with headline:
"From Concept to Capacity – Your Self Storage Experts"
• Subheadline: “Keystone Vault Depot Services delivers turnkey design, construction, leasing, and management services for profitable self storage operations.”
• Quick Service Icons:
o Facility Design & Development
o Construction & Build Management
o Lease-Up & Marketing
o Ongoing Facility Management
• Call to Action Button: “LEARN MORE” → links to ABOUT US page.
• Featured Project Highlights: Showcase a few completed or current projects with photos and stats.
• Contact Banner: “Ready to build your next self storage project? Let’s talk.” → CONTACT page.
2. ABOUT US
Purpose: Build credibility, showcase experience, and explain the value proposition.
Content Highlights:
• Who We Are: Overview of Keystone Vault Depot Services’ history, mission, and team expertise.
• Our Approach: End-to-end process from site selection to occupancy.
• Why Choose Us:
o Industry expertise in self storage
o Proven track record in lease-up success
o Strong vendor and contractor network
3. SERVICES
Purpose: Detail all service offerings with clarity and authority.
Sections:
• Design & Development: Market analysis, site planning, and architectural design.
• Construction Management: Overseeing timelines, budgets, and quality control.
• Lease-Up Strategy: Marketing, promotions, and occupancy acceleration.
• Ongoing Facility Management: Staffing, maintenance, revenue optimization.

4. CONTACT
Purpose: Provide simple, direct ways to connect.
Content Highlights:
• Contact Form (Name, Email, Phone, Message)
• Direct Email: info@keystonevaultdepot.com
• Phone (if applicable)
• Google Map embed (if there’s a head office location)
• CTA: “Let’s Build Your Storage Success Story.”
Design & Technical Notes
• Visual Style: Clean, modern, bold typography, professional color palette (to be based on branding), strong imagery of self storage facilities.
• Performance: Image compression, caching, responsive scaling.
• SEO Targets: “Self storage facility developer,” “self storage construction,” “self storage management company,” “lease-up services for self storage.”

WordPress or Joomla – must be desktop and mobile friendly with fast page load speed. Need the ability to edit ourselves.

Use pantone colours - #033c5a – dark blue
#2baadf – light blue

```html
<!DOCTYPE html>
<html lang="en">
<head>
<meta charset="utf-8">
<title>Keystone Vault Depot Services – Self Storage Experts</title>
<link href="https://fonts.googleapis.com/css2?family=Inter:wght@400;500;600&display=swap" rel="stylesheet">
<style>
:root{
  --navy:#033c5a;
  --sky:#2baadf;
  --hero-bg:#eff9fb;
  --text:#1f2d36;
  --muted:#3b4a55;
  --white:#ffffff;
  --line:#cfe3ec;
}
*{box-sizing:border-box;margin:0;padding:0}
html,body{width:1200px;height:3341px;overflow:hidden}
body{font-family:'Inter',sans-serif;color:var(--text);background:var(--white);position:relative}
a{color:inherit;text-decoration:none}
.brand{display:flex;align-items:center;gap:8px;font-size:15px;font-weight:600;color:var(--navy);line-height:1.1}
.brand-mark{width:22px;height:22px;background:var(--navy);border-radius:3px;flex:none}
.btn{display:flex;align-items:center;justify-content:center;border-radius:8px;font-size:20px}
.btn-outline{border:1.5px solid var(--navy);color:var(--navy);background:transparent}
.btn-sky{background:var(--sky);color:var(--white)}
.btn-white{background:var(--white);color:var(--navy)}
h1,h2{font-weight:600;text-align:center;line-height:1.18}

/* header */
.site-header{position:absolute;top:0;left:0;width:1200px;height:84px;display:flex;align-items:center;padding:0 42px}
.main-nav{display:flex;gap:0;margin-left:38px;font-size:13.5px;color:var(--text)}
.main-nav a{margin-right:27px}
.header-cta{position:absolute;left:1032px;top:25px;width:124px;height:35px;font-size:13.5px;border-radius:10px}

/* hero */
.hero{position:absolute;top:84px;left:0;width:1200px;height:1006px;background:var(--hero-bg)}
.hero h1{position:absolute;top:72px;width:100%;font-size:44px;color:var(--navy)}
.hero-sub{position:absolute;top:196px;width:100%;text-align:center;font-size:22.5px;line-height:1.22;color:var(--navy)}
.hero .btn{position:absolute;left:527px;top:288px;width:181px;height:40px;font-size:19px}
.hero-photo{position:absolute;left:140px;top:367px;width:955px;height:563px;border-radius:10px;
  background:linear-gradient(180deg,#c9d3da 0%,#dfe5e9 45%,#9fb9c2 75%,#8d8a86 100%)}

/* services */
.services{position:absolute;top:1090px;left:0;width:1200px;height:604px}
.services h2{position:absolute;top:82px;width:100%;font-size:44px;color:var(--navy)}
.services-sub{position:absolute;top:197px;width:100%;text-align:center;font-size:22.5px;line-height:1.22;color:var(--navy)}
.services .btn{position:absolute;left:508px;top:281px;width:183px;height:44px}
.service-strip{position:absolute;left:122px;top:356px;width:956px;height:164px;border:1px solid var(--line);border-radius:10px;
  background:radial-gradient(ellipse at 50% 40%,#dff2fb 0%,#f2fafd 70%);display:flex}
.service-item{position:absolute;top:0;width:220px;margin-left:-110px;text-align:center;color:var(--navy);font-size:20px;line-height:1.2}
.service-item svg{display:block;margin:30px auto 12px;width:36px;height:36px}

/* projects */
.projects{position:absolute;top:1694px;left:0;width:1200px;height:852px;background:var(--navy);color:var(--white)}
.projects h2{position:absolute;top:112px;width:100%;font-size:44px}
.projects-sub{position:absolute;top:177px;width:100%;text-align:center;font-size:22.5px;line-height:1.22}
.project-card{position:absolute;top:298px;width:296px;height:358px;background:var(--white);border-radius:8px;color:var(--navy);padding:20px}
.project-photo{width:256px;height:234px;border-radius:8px}
.project-name{margin-top:10px;font-size:18px;line-height:1.4;padding-left:3px}
.project-stats{margin-top:2px;font-size:11.5px;line-height:1.25;padding-left:3px}
.projects .btn{position:absolute;left:499px;top:726px;width:201px;height:42px}

/* cta */
.cta{position:absolute;top:2546px;left:0;width:1200px;height:457px;
  background:linear-gradient(90deg,#3d5f78 0%,#6a7a7f 18%,#8c6a48 40%,#7b5a3e 65%,#97704a 85%,#5b6a70 100%)}
.cta-card{position:absolute;left:170px;top:68px;width:860px;height:323px;background:var(--white);border-radius:20px}
.cta-card h2{position:absolute;top:38px;width:100%;font-size:44px;color:var(--navy)}
.cta-sub{position:absolute;top:151px;width:100%;text-align:center;font-size:22.5px;line-height:1.22;color:var(--navy)}
.cta-card .btn{position:absolute;left:338px;top:242px;width:183px;height:43px}

/* footer */
.site-footer{position:absolute;top:3003px;left:0;width:1200px;height:338px;font-size:14.5px;color:var(--text)}
.footer-brand{position:absolute;left:48px;top:72px}
.footer-tag{position:absolute;left:37px;top:116px;font-size:15px}
.social{position:absolute;left:51px;top:155px;display:flex;gap:12px}
.social span{width:20px;height:20px;border-radius:50%;background:#111}
.footer-col{position:absolute;top:68px;list-style:none}
.footer-col li{height:34px;line-height:20px}
.footer-col .col-title{font-weight:500}
.col-links{left:306px}
.col-contact{left:476px}
.legal{position:absolute;left:843px;top:59px;font-size:12.5px;line-height:28px}
.legal a{color:var(--navy)}
</style>
</head>
<body>

<header class="site-header">
  <a class="brand" href="#"><span class="brand-mark"></span>Keystone Vault Depot Services</a>
  <nav class="main-nav"><a href="#">Home</a><a href="#">Services</a><a href="#">Project</a><a href="#">About</a></nav>
  <a class="btn btn-outline header-cta" href="#">Contact us</a>
</header>

<section class="hero">
  <h1>From Concept to Capacity<br>Your Self Storage Experts</h1>
  <p class="hero-sub">Keystone Vault Depot Services delivers turnkey design, construction, leasing,<br>and management services for profitable self storage operations</p>
  <a class="btn btn-outline" href="#">Learn More</a>
  <div class="hero-photo" role="img" aria-label="Modern self storage facility with a covered loading bay and blue glass windows"></div>
</section>

<section class="services">
  <h2>Comprehensive Self Storage<br>Services</h2>
  <p class="services-sub">From design to daily operations, our team delivers end-to-<br>end solutions for profitable self storage facilities</p>
  <a class="btn btn-sky" href="#">Learn More</a>
  <div class="service-strip">
    <div class="service-item" style="left:130px">
      <svg viewBox="0 0 24 24" fill="none" stroke="currentColor" stroke-width="1.5"><path d="M9 18h5M10 21h3M12 3a6 6 0 0 0-3.5 10.9V16h6v-2.1A6 6 0 0 0 12 3z"/><path d="M19 2l.7 1.5L21 4l-1.3.6L19 6l-.7-1.4L17 4l1.3-.5z"/></svg>
      Facility Design &amp;<br>Development</div>
    <div class="service-item" style="left:366px">
      <svg viewBox="0 0 24 24" fill="none" stroke="currentColor" stroke-width="1.5"><path d="M3 7l7-4 7 4v5M3 7v8l7 4M3 7l7 4 7-4M10 11v8"/><circle cx="18" cy="18" r="2.5"/><path d="M18 14v1.2M18 20.8V22M14 18h1.2M20.8 18H22"/></svg>
      Construction &amp; Build<br>Management</div>
    <div class="service-item" style="left:602px">
      <svg viewBox="0 0 24 24" fill="none" stroke="currentColor" stroke-width="1.5"><rect x="3" y="7" width="18" height="13" rx="1.5"/><path d="M9 7V4h6v3M6 14h3l2-3 2 5 2-2h3"/></svg>
      Lease-Up &amp;<br>Marketing</div>
    <div class="service-item" style="left:826px">
      <svg viewBox="0 0 24 24" fill="none" stroke="currentColor" stroke-width="1.5"><path d="M2 8l4-2 6 3 6-3 4 2M6 11l4 3c1 .8 2 .8 3 0l5-4M8 14l3 3c.6.6 1.4.6 2 0l3-3"/></svg>
      Ongoing Facility<br>Management</div>
  </div>
</section>

<section class="projects">
  <h2>Featured Projects</h2>
  <p class="projects-sub">Explore some of our recent developments that showcase<br>quality, efficiency, and profitability</p>
  <article class="project-card" style="left:121px">
    <div class="project-photo" role="img" aria-label="Contemporary storage building exterior at dusk" style="background:linear-gradient(180deg,#8ba4b8 0%,#c9c3bd 50%,#6a4f4a 80%,#3b3438 100%)"></div>
    <p class="project-name">Ridgeline Storage<br>Chicago, Illinois</p>
    <p class="project-stats">320 Units | Opened 2022 | 92% Occupancy in<br>8 Months</p>
  </article>
  <article class="project-card" style="left:451px">
    <div class="project-photo" role="img" aria-label="Warehouse interior with racking and skylights" style="background:linear-gradient(180deg,#5f6a72 0%,#9aa3a8 45%,#6c6f70 75%,#3f4243 100%)"></div>
    <p class="project-name">Ridgeline Storage<br>Chicago, Illinois</p>
    <p class="project-stats">320 Units | Opened 2022 | 92% Occupancy in<br>8 Months</p>
  </article>
  <article class="project-card" style="left:782px">
    <div class="project-photo" role="img" aria-label="Indoor corridor lined with green storage unit doors" style="background:linear-gradient(90deg,#7fb55a 0%,#a9cf86 25%,#dfe3e2 50%,#a9cf86 75%,#7fb55a 100%)"></div>
    <p class="project-name">Ridgeline Storage<br>Chicago, Illinois</p>
    <p class="project-stats">320 Units | Opened 2022 | 92% Occupancy in<br>8 Months</p>
  </article>
  <a class="btn btn-white" href="#">See All Project</a>
</section>

<section class="cta" role="img" aria-label="Row of blue-door outdoor storage units beside autumn trees">
  <div class="cta-card">
    <h2>Ready to Build Your Next Self<br>Storage Project?</h2>
    <p class="cta-sub">Let’s discuss how Keystone Vault Depot Services can help you design,<br>construct, and manage a facility that maximizes returns</p>
    <a class="btn btn-sky" href="#">Contact Us</a>
  </div>
</section>

<footer class="site-footer">
  <a class="brand footer-brand" href="#"><span class="brand-mark"></span>Keystone Vault Depot Services</a>
  <p class="footer-tag">From Concept to Capacity</p>
  <div class="social" aria-label="Social links"><span></span><span></span><span></span><span></span></div>
  <ul class="footer-col col-links">
    <li class="col-title">Quick Links</li>
    <li><a href="#">Home</a></li><li><a href="#">About Us</a></li><li><a href="#">Services</a></li><li><a href="#">Project</a></li><li><a href="#">Contact Us</a></li>
  </ul>
  <ul class="footer-col col-contact">
    <li class="col-title">Contact Info</li>
    <li>Address: 10458 82 Ave, Edmonton, AB T6E 2K9</li>
    <li>Email: info@keystonevaultdepot.com</li>
    <li>Phone: +[country code] [number]</li>
  </ul>
  <div class="legal">
    <p>© 2025 Keystone Vault Depot Services. All Rights Reserved</p>
    <p><a href="#">Privacy Policy</a> | <a href="#">Terms &amp; Conditions</a></p>
  </div>
</footer>

</body>
</html>
```